Velmora Land Surveying Website Design

We are working with Velmora. They are a national land surveying company and in need of a new website design.

Some sites to use for inspiration:

https://brannockeng.com
https://www.qlvinc.com
https://dervanto.com
https://gkw.us
https://corvenbuilt.com
https://www.pellacombwendrix.com

Thank you for taking the time to consider designing a website for us. We are web developers based in Stockton and Los Angeles, CA, USA. Most of our projects go through the same process. Understanding this process may help you win a project with us. We custom-code all of our websites in-house. We don’t have any requirements as to what tools you use for your design, but we prefer Figma files. For any design that we label as four-stars, we send it to the client for review. The client picks the final design they want us to use. Once we complete this process, we will continue to show additional clients all the four-star sites and purchase them later. Your designs will have multiple chances to sell. For better chances of success, we ask that you follow these guidelines.

IMAGES:
If you use any images or icons in the design, we ask that you have a link to the asset so we can purchase the image/icon. Most of the designs we submit do not have the customer’s images on them unless they have some great images. Be creative; show us the feeling you are trying to portray with your image choices. Use any royalty-free site you choose. We subscribe to Quillar and mainly use their images, but we can purchase images outside of Quillar.

PLEASE NOTE: we will not submit designs to clients with watermarks on the images.

FONTS:
We ask that you identify the fonts used in the design. This can be done in a message if you want. We typically use Google Fonts and Quillar Fonts.

CONTENT:
We're always open to different content and ideas. We often submit designs with stock images so the client can see our vision. We typically take pictures after the website launch to use their images with our vision. Lorem Ipsum is fine for paragraphs, but we ask that you write the headers in correct English. We want to be able to show the vision and identify the sections of the website.

INSPIRATION:
We typically add a couple of links in the brief of websites we like to help you get started in your design.

REVISIONS:
We do not often ask for revisions of the designs unless we see something in the design that may not appeal to the client. If there are slight changes that we want to make, we do that in the development process.

FEEDBACK:
We rarely give feedback on designs during the design process. We are working on many website projects and do not have the time to provide feedback. We usually respond if your request is well thought out and asks specific questions, but a note asking “feedback, please” usually goes unanswered.

```html
<!DOCTYPE html>
<html lang="en">
<head>
<meta charset="utf-8">
<title>Velmora Land Surveying</title>
<link href="https://fonts.googleapis.com/css2?family=Bebas+Neue&family=Montserrat:wght@400;500;600;700&display=swap" rel="stylesheet">
<style>
:root{
  --navy:#0f2552;
  --red:#e2412f;
  --red-deep:#c0281c;
  --mint:#f4f8f1;
  --grey-bg:#e4e4e4;
  --text:#5a6275;
  --white:#ffffff;
  --line:#e3e3e3;
}
*{box-sizing:border-box;margin:0;padding:0}
html,body{width:1187px;height:1200px;overflow:hidden;background:var(--grey-bg)}
body{font-family:"Montserrat",sans-serif;color:var(--navy)}
.page{position:absolute;left:443px;top:25px;width:962px;height:3680px;background:var(--white);transform:scale(.3125);transform-origin:top left;overflow:hidden}
.abs{position:absolute}
.display{font-family:"Bebas Neue",sans-serif;font-weight:400;line-height:.95;color:var(--navy)}
.accent{color:var(--red)}
p{font-size:11px;line-height:1.6;color:var(--text)}
.brand{font-weight:700;color:var(--red);font-size:16px;letter-spacing:.3px;display:flex;align-items:center;gap:8px}
.brand .dot{width:24px;height:24px;border-radius:50%;background:var(--red)}

/* top bar */
.topbar{left:0;top:0;width:962px;height:20px;background:var(--navy);color:#fff;font-size:8px;display:flex;align-items:center;padding:0 64px;gap:18px}
.topbar .social{margin-left:auto;display:flex;gap:6px;align-items:center}
.topbar .social i{width:8px;height:8px;border-radius:50%;background:#fff;display:block}

/* header */
.header{left:0;top:20px;width:962px;height:82px;display:flex;align-items:center;padding:0 64px}
.nav{margin-left:auto;display:flex;gap:18px;align-items:center;font-size:10px;font-weight:500}
.nav .active{border:1px solid var(--red);border-radius:20px;padding:8px 16px}
.phone-btn{margin-left:26px;background:var(--red);color:#fff;border-radius:20px;padding:9px 20px;font-size:11px;font-weight:600;display:flex;gap:6px;align-items:center}

/* hero */
.hero{left:0;top:102px;width:962px;height:418px;overflow:hidden;
  background:linear-gradient(180deg,#c3d5e8 0%,#dfe8f1 35%,#eef1f4 62%,#eceee8 80%,#b9b77a 90%,#7f8a3e 100%)}
.hero-photo{left:560px;top:0;width:402px;height:418px;
  background:
    radial-gradient(ellipse 34% 20% at 70% 12%,rgba(214,170,40,.75),rgba(214,170,40,0) 70%),
    radial-gradient(ellipse 30% 26% at 72% 34%,rgba(150,140,125,.85),rgba(150,140,125,0) 75%),
    radial-gradient(ellipse 22% 18% at 80% 38%,rgba(230,90,60,.55),rgba(230,90,60,0) 75%),
    radial-gradient(ellipse 28% 32% at 76% 70%,rgba(110,140,180,.8),rgba(110,140,180,0) 75%),
    radial-gradient(ellipse 14% 48% at 38% 58%,rgba(200,150,60,.6),rgba(200,150,60,0) 75%),
    linear-gradient(180deg,rgba(0,0,0,0) 82%,rgba(120,135,60,.6) 100%)}
.hero h1{left:66px;top:50px;font-size:94px}
.hero p{left:66px;top:232px;width:390px;color:#3a4256}
.btn{font-size:11px;font-weight:600;color:#fff;border-radius:18px;padding:9px 22px;display:inline-block}
.btn-red{background:var(--red)}
.btn-navy{background:var(--navy)}
.hero .actions{left:66px;top:300px;display:flex;gap:12px}

/* feature cards */
.feature{top:610px;width:270px;height:236px;border:2px solid var(--red);border-radius:12px;background:var(--mint);text-align:center;padding-top:50px}
.feature svg{display:block;margin:0 auto 14px}
.feature h3{font-size:14px;font-weight:600;margin-bottom:14px}
.feature p{width:190px;margin:0 auto;font-size:10px}

/* about */
.about-photo{left:64px;top:934px;width:408px;height:308px;border-radius:12px;
  background:
    radial-gradient(ellipse 26% 14% at 52% 44%,rgba(70,120,40,.95),rgba(70,120,40,0) 80%),
    radial-gradient(ellipse 34% 16% at 52% 52%,rgba(120,170,70,.95),rgba(120,170,70,0) 85%),
    radial-gradient(ellipse 32% 10% at 52% 64%,rgba(120,85,55,.8),rgba(120,85,55,0) 85%),
    linear-gradient(180deg,#f7f8f5,#fdfdfc);
  box-shadow:0 6px 20px rgba(0,0,0,.12)}
.stats{left:104px;top:1242px;width:326px;height:106px;background:var(--red);border-radius:0 0 10px 10px;display:flex;padding:26px 40px;gap:40px;color:#fff}
.stats b{font-family:"Bebas Neue",sans-serif;font-weight:400;font-size:32px;display:block;line-height:1}
.stats span{font-size:10px}
.about h2{left:532px;top:964px;font-size:36px}
.about .copy{left:532px;top:1054px;width:330px}
.about .copy p{margin-bottom:10px;font-size:10.5px}

/* services */
.services h2{left:64px;top:1428px;font-size:36px}
.arrows{display:flex;gap:12px;font-size:16px;color:var(--navy)}
.svc{top:1498px;width:212px}
.svc .img{height:278px;border-radius:10px}
.svc h4{font-size:13px;font-weight:700;margin:50px 0 10px}
.svc p{font-size:10px;width:190px}
.svc.raised h4{margin-top:38px}
.svc .overlay{height:232px;border-radius:10px;color:#fff;padding:150px 28px 0;font-size:10px;line-height:1.5;position:relative;
  background:radial-gradient(ellipse at 60% 40%,#ea6a58,#e2412f 60%,#d8392a)}
.divider{left:64px;top:1960px;width:834px;height:1px;background:var(--line)}
.partner{top:2032px;width:30px;height:28px;border-radius:50%;background:#8a8f99;opacity:.7}

/* testimonial */
.testimonial{left:0;top:2138px;width:962px;height:460px;overflow:hidden;background:linear-gradient(135deg,#d93a28,#c3281c 60%,#b8251a)}
.quote-mark{left:24px;top:0;font-family:"Bebas Neue",sans-serif;font-size:300px;color:#f0907f;line-height:1}
.person{left:40px;top:40px;width:500px;height:420px;
  background:
    radial-gradient(ellipse 16% 11% at 52% 16%,rgba(245,245,240,.95),rgba(245,245,240,0) 80%),
    radial-gradient(ellipse 12% 12% at 52% 30%,rgba(190,130,100,.7),rgba(190,130,100,0) 80%),
    radial-gradient(ellipse 34% 34% at 64% 72%,rgba(215,230,60,.9),rgba(215,230,60,0) 75%),
    radial-gradient(ellipse 24% 26% at 82% 66%,rgba(50,80,130,.85),rgba(50,80,130,0) 80%),
    radial-gradient(ellipse 16% 14% at 22% 62%,rgba(200,210,220,.85),rgba(200,210,220,0) 80%)}
.testimonial .body{left:554px;top:74px;width:340px;color:#fff}
.testimonial .stars{font-size:12px;letter-spacing:3px}
.testimonial p{color:#fff;font-size:10.5px;margin-top:44px}
.testimonial p+p{margin-top:10px}
.testimonial h5{font-size:12px;margin-top:40px}
.testimonial .role{font-size:10px;margin-top:8px}

/* blog */
.blog h2{left:0;width:962px;top:2698px;text-align:center;font-size:36px}
.post{top:2788px;width:270px}
.post .img{height:236px;border-radius:14px;position:relative}
.post .img span{position:absolute;right:20px;top:16px;color:#fff;font-size:14px}
.post .card{position:relative;background:#fff;width:226px;margin-top:-54px;border-radius:0 14px 0 0;padding:14px 14px 0}
.post h4{font-size:13px;font-weight:700}
.post .date{font-size:9px;color:var(--red);font-weight:600;margin:8px 0 14px}
.post p{font-size:10px}
.post .more{font-size:10px;color:var(--red);font-weight:600;margin-top:14px}

/* footer */
.footer{left:0;top:3294px;width:962px;height:386px;background:var(--navy);color:#fff}
.footer-badge{left:460px;top:3270px;width:42px;height:42px;border-radius:50%;background:var(--red)}
.footer .about-col{left:64px;top:56px;width:250px}
.footer .about-col p{color:#fff;font-size:9.5px;margin-top:26px}
.footer .social{display:flex;gap:8px;margin-top:20px}
.footer .social i{width:28px;height:28px;border-radius:50%;border:1.5px solid #fff;display:block}
.footer h6{font-size:13px;font-weight:600;margin-bottom:26px}
.footer ul{list-style:none;font-size:9.5px;line-height:2.4}
.footer .links{left:464px;top:58px}
.footer .addr{left:716px;top:58px;width:190px;font-size:9.5px}
.footer .addr div{display:flex;gap:8px;margin-bottom:16px;align-items:flex-start}
.footer .rule{left:64px;top:290px;width:834px;height:1px;background:rgba(255,255,255,.2)}
.footer .copy{left:0;width:962px;top:336px;text-align:center;font-size:9px}
</style>
</head>
<body>
<div class="page">

  <div class="abs topbar">
    <span>◷ Monday - Friday 8AM - 9PM</span>
    <span>⌖ Offices Harrowgate Square, London WC9 2ZQ</span>
    <span class="social">Visit our social pages <i></i><i></i><i></i></span>
  </div>

  <header class="abs header">
    <div class="brand"><span class="dot"></span>Velmora Land Surveying</div>
    <nav class="nav">
      <span class="active">Home</span><span>About</span><span>Services</span><span>Careers</span><span>News</span><span>Contact</span>
    </nav>
    <span class="phone-btn">
      <svg width="12" height="8" viewBox="0 0 12 8"><path d="M1 5c2-4 8-4 10 0l-2 2-2-1V4H5v2L3 7z" fill="#fff"/></svg>123 456 7890
    </span>
  </header>

  <section class="abs hero">
    <div class="abs hero-photo" role="img" aria-label="Surveyor in a yellow hard hat looking through a theodolite on a tripod in a grassy field"></div>
    <h1 class="abs display">National<br><span class="accent">Land</span> Surveying</h1>
    <p class="abs">Land survey is a vital start to a broad spectrum of projects – and it needs to be conducted quickly, accurately and to deliver as much data as possible to inform the next step.</p>
    <div class="abs actions"><span class="btn btn-red">View Portfolio</span><span class="btn btn-navy">Learn More</span></div>
  </section>

  <div class="abs feature" style="left:64px">
    <svg width="56" height="44" viewBox="0 0 56 44" fill="none" stroke="#e2412f" stroke-width="2"><path d="M4 6h20M32 6h20M14 6v8h28V6M18 14l-4 18M38 14l4 18M22 22h12"/></svg>
    <h3>LiDAR Survey</h3><p>Lorem Ipsum is simply dummy text of the printing</p>
  </div>
  <div class="abs feature" style="left:346px;padding-top:44px">
    <svg width="40" height="56" viewBox="0 0 40 56" fill="none" stroke="#e2412f" stroke-width="2"><rect x="8" y="2" width="24" height="52" rx="5"/><circle cx="20" cy="12" r="2"/></svg>
    <h3>Mobile Mapping</h3><p>Lorem Ipsum is simply dummy text of the printing</p>
  </div>
  <div class="abs feature" style="left:628px">
    <svg width="48" height="48" viewBox="0 0 48 48" fill="none" stroke="#e2412f" stroke-width="2"><path d="M24 4 42 14v20L24 44 6 34V14z M6 14l18 10 18-10 M24 24v20"/></svg>
    <h3>Topographic Survey</h3><p>Lorem Ipsum is simply dummy text of the printing</p>
  </div>

  <section class="about">
    <div class="abs about-photo" role="img" aria-label="Cut-away block of grassy land with trees showing soil layers"></div>
    <div class="abs stats">
      <div><b>140+</b><span>Successful Projects</span></div>
      <div><b>38+</b><span>Team Members</span></div>
    </div>
    <h2 class="abs display">Trusted General Contracting<br>Across <span class="accent">California</span></h2>
    <div class="abs copy">
      <p>Lorem Ipsum is simply dummy text of the printing and typesetting industry. Lorem Ipsum has been the industry's standard dummy text ever since the 1500s, when an unknown printer took a galley of type and scrambled it to make a type specimen book.</p>
      <p>It has survived not only five centuries, but also the leap into electronic typesetting, remaining essentially unchanged. Contrary to popular belief, Lorem Ipsum is not simply random text. It has roots in a piece of classical Latin literature from 45 BC, making it over 2000 years old.</p>
      <p>Edwin Marlow, a Latin professor at Ashbury College in Virginia, looked.</p>
    </div>
  </section>

  <section class="services">
    <h2 class="abs display">Our <span class="accent">Services</span></h2>
    <div class="abs arrows" style="left:872px;top:1436px"><span>‹</span><span>›</span></div>
    <div class="abs svc" style="left:64px">
      <div class="img" role="img" aria-label="Aerial view of green farm fields" style="background:linear-gradient(165deg,#4f7a34 0%,#7fae4e 30%,#5c8a38 50%,#9a6a48 75%,#7a4a34 100%)"></div>
      <h4>Design</h4><p>Lorem Ipsum is simply dummy text of the printing</p>
    </div>
    <div class="abs svc raised" style="left:286px">
      <div class="overlay">Lorem Ipsum is simply dummy text of the printing<span style="position:absolute;right:20px;top:18px">↗</span></div>
      <h4>Construction</h4><p>Lorem Ipsum is simply dummy text of the printing</p>
    </div>
    <div class="abs svc" style="left:508px">
      <div class="img" role="img" aria-label="Aerial view of forest with winding paths" style="background:radial-gradient(ellipse at 40% 45%,#5f7a3e,#3a5428 55%,#2d4420)"></div>
      <h4>Careers</h4><p>Lorem Ipsum is simply dummy text of the printing</p>
    </div>
    <div class="abs svc" style="left:730px">
      <div class="img" role="img" aria-label="Hand placing red pins on a printed map" style="background:radial-gradient(ellipse 40% 30% at 35% 20%,#d9a48e,rgba(217,164,142,0) 80%),radial-gradient(ellipse 40% 14% at 55% 82%,rgba(220,60,60,.55),rgba(220,60,60,0) 80%),linear-gradient(180deg,#f1ece8,#e6e9ee)"></div>
      <h4>Engineering</h4><p>Lorem Ipsum is simply dummy text of the printing</p>
    </div>
    <div class="abs svc" style="left:952px">
      <div class="img" role="img" aria-label="Surveying photo" style="background:linear-gradient(160deg,#a9b2a4,#7d8a78)"></div>
    </div>
  </section>

  <div class="abs divider"></div>
  <div class="abs partner" style="left:156px"></div>
  <div class="abs partner" style="left:282px"></div>
  <div class="abs partner" style="left:414px;height:8px;top:2042px;width:46px;border-radius:4px"></div>
  <div class="abs partner" style="left:536px;border-radius:6px"></div>
  <div class="abs partner" style="left:648px;height:16px;top:2038px;width:58px;border-radius:4px"></div>
  <div class="abs partner" style="left:776px;height:18px;top:2038px;width:44px;border-radius:3px"></div>

  <section class="abs testimonial">
    <div class="abs quote-mark">“</div>
    <div class="abs person" role="img" aria-label="Site engineer in a white hard hat and safety vest using a tablet"></div>
    <div class="abs arrows" style="left:866px;top:70px;color:#fff"><span>‹</span><span>›</span></div>
    <div class="abs body">
      <div class="stars">★★★★★</div>
      <p>Lorem Ipsum is simply dummy text of the printing and typesetting industry. Lorem Ipsum has been the industry's standard dummy text ever since the 1500s, when an unknown printer took a galley of type and scrambled it to make a type specimen book.</p>
      <p>It has survived not only five centuries, but also the leap into electronic typesetting, remaining essentially unchanged. Contrary to popular belief, Lorem Ipsum is not simply random text.</p>
      <h5>R. Calder</h5>
      <div class="role">Office Building Owner</div>
    </div>
  </section>

  <section class="blog">
    <h2 class="abs display">Recent <span class="accent">Blog</span> Posts</h2>
    <div class="abs post" style="left:66px">
      <div class="img" role="img" aria-label="Total station surveying instrument beside a road" style="background:radial-gradient(ellipse 18% 30% at 22% 50%,rgba(220,170,40,.8),rgba(220,170,40,0) 80%),linear-gradient(180deg,#d49a94,#b49aa6 45%,#7b7f92 70%,#3f4656)"><span>↗</span></div>
      <div class="card"><h4>Projects that reflect</h4><div class="date">▣ 24-09-25</div><p>Lorem Ipsum is simply dummy text of the printing</p><div class="more">Read More →</div></div>
    </div>
    <div class="abs post" style="left:348px">
      <div class="img" role="img" aria-label="Hands holding a tablet showing a survey map" style="background:radial-gradient(ellipse 34% 28% at 50% 50%,rgba(120,140,110,.9),rgba(120,140,110,0) 80%),linear-gradient(160deg,#e8764a,#b5663f 50%,#5b4a3e)"><span>↗</span></div>
      <div class="card"><h4>Projects that reflect</h4><div class="date">▣ 24-09-25</div><p>Lorem Ipsum is simply dummy text of the printing</p><div class="more">Read More →</div></div>
    </div>
    <div class="abs post" style="left:630px">
      <div class="img" role="img" aria-label="Surveyor reading plans in a wheat field" style="background:radial-gradient(ellipse 10% 26% at 30% 55%,rgba(60,80,120,.6),rgba(60,80,120,0) 80%),linear-gradient(180deg,#c6a2c8,#d8b2b0 35%,#c8b070 58%,#9c8a42)"><span>↗</span></div>
      <div class="card"><h4>Projects that reflect</h4><div class="date">▣ 24-09-25</div><p>Lorem Ipsum is simply dummy text of the printing</p><div class="more">Read More →</div></div>
    </div>
    <div class="abs arrows" style="left:466px;top:3170px"><span>‹</span><span>›</span></div>
  </section>

  <footer class="abs footer">
    <div class="abs about-col">
      <div class="brand"><span class="dot"></span>Velmora Land Surveying</div>
      <p>Lorem Ipsum is simply dummy text of the printing and typesetting industry. Lorem Ipsum has been the industry's standard dummy text ever.</p>
      <div class="social"><i></i><i></i><i></i></div>
    </div>
    <div class="abs links">
      <h6>Quick Links</h6>
      <ul><li>Home</li><li>About</li><li>Services</li><li>Careers</li><li>News</li><li>Contact</li></ul>
    </div>
    <div class="abs addr">
      <h6>Address</h6>
      <div><svg width="9" height="12" viewBox="0 0 9 12"><path d="M4.5 0A4.5 4.5 0 0 0 0 4.5C0 8 4.5 12 4.5 12S9 8 9 4.5A4.5 4.5 0 0 0 4.5 0z" fill="#fff"/><circle cx="4.5" cy="4.5" r="1.6" fill="#0f2552"/></svg><span>2180 Larkmoor Rd Ste 40, Fernbrook, Melbourne</span></div>
      <div><svg width="10" height="10" viewBox="0 0 10 10"><path d="M2 0l2 3-1 1c1 2 2 3 3 3l1-1 3 2-1 2C4 10 0 6 0 2z" fill="#fff"/></svg><span>(123) 456-7890</span></div>
      <div><svg width="11" height="8" viewBox="0 0 11 8"><rect width="11" height="8" rx="1" fill="#fff"/><path d="M0 0l5.5 4L11 0" stroke="#0f2552" fill="none"/></svg><span>sales@velmora.com</span></div>
    </div>
    <div class="abs rule"></div>
    <div class="abs copy">© 2025 Velmora Land Surveying. All rights reserved.</div>
  </footer>
  <div class="abs footer-badge"></div>

</div>
</body>
</html>
```